Marketing Agency Needs Fresh New Look

QuillBeaconWorks.com is a Digital Marketing agency with locations in North Carolina and Florida. And, yes, we do custom Websites too. When we're designing for ourselves, we prefer to outsource because we typically get fresher perspectives from designers involved in the project. Which is why we're here today posting this Redesign project for our very own website.

Overall, we like our website look/feel....but don't LOVE it. We need our new site to be a bit fresher and more current using some of today's web design/development trends.

Some of the details: We want to use more current font styles and sizes (ideally, we use 3 different fonts including one "handwritten" or script font). We use the little nerdy scientist way too much throughout our website. We want to project a positive, friendly image to our customers....but we also want to be considered serious professionals in our industry(s). So, we would like to see a better mix of fun & friendly with professional & completely capable.

Here are two examples of our local competitors and websites that we think are very well done and include some of elements we're looking to see on our new site:

1) www.pixelmongrels.com = these guys do a great job at mixing their cartoony dinosaur with realism imagery. Very clean & professional website, but also cool and interesting how they carry through some of their branding and toony graphic elements. We like the use of big circles to highlight certain elements. We feel that this would play well for us too because we already use some of these big circles/bubbles in our bokeh background.

2) www.vantoloweb.com = these guys have the same kind of top to bottom layout with big chunks for each section. They come across as a little more "buttoned up" then pixelmongrels, but still friendly enough to make a small business owner feel comfortable.

There are a few elements that we consider part of our brand and that we want to continue to use in our new design. They are as follows:
1) The nerdy scientist dude....we have 50+ variations of this little guy in every file format you need. I'll try to upload the whole set....at the least, you'll have one or two examples.

2) The electric green bokeh background you see at the top of each page of our website.

3) And our logo of course which is included in uploads.

Please feel free to ask me any questions. We're really open to new and fresh ideas and creativity. So...let 'r rip!

```html
<!DOCTYPE html>
<html lang="en">
<head>
<meta charset="utf-8">
<title>QuillBeaconWorks – Digital Marketing</title>
<link rel="stylesheet" href="https://fonts.googleapis.com/css2?family=Open+Sans:wght@400;600;700;800&display=swap">
<style>
:root{
  --orange:#f28a16;
  --orange-dark:#e06f06;
  --green:#5aaa1c;
  --green-dark:#3f8a12;
  --lime:#8fd11e;
  --sky:#2ec2f0;
  --ink:#2b2b2b;
  --text:#666;
  --soft:#f2f2f2;
  --footer:#1f1f1f;
  --footer-text:#9a9a9a;
  --skin:#e4bc98;
  --suit:#2c323c;
}
*{margin:0;padding:0;box-sizing:border-box}
html,body{width:1200px;height:3607px;overflow:hidden}
body{font-family:"Open Sans",Arial,sans-serif;color:var(--text);background:#fff;position:relative}
section,header,footer{position:absolute;left:0;width:1200px}
.btn{position:absolute;display:flex;align-items:center;justify-content:center;color:#fff;font-weight:600;font-size:15px;border-radius:3px}
.btn-orange{background:linear-gradient(#f9a233,var(--orange-dark))}
.btn-green{background:linear-gradient(#6cbd27,var(--green-dark))}
.section-title{position:absolute;left:0;width:1200px;text-align:center;color:var(--ink);font-size:30px;font-weight:600}
.section-sub{position:absolute;left:0;width:1200px;text-align:center;font-size:13px;color:#777}

/* header */
.topbar{top:0;height:84px;background:linear-gradient(#f9a02a,#ec7f0c);z-index:3}
.logo{position:absolute;left:125px;top:0;width:175px;height:140px;background:#fff;border-radius:0 0 8px 8px;box-shadow:0 2px 6px rgba(0,0,0,.25);display:flex;flex-direction:column;align-items:center;justify-content:center;gap:8px}
.logo-dot{width:30px;height:30px;border-radius:50%;background:var(--green)}
.logo-name{font-size:17px;font-weight:700;color:var(--green-dark)}
.nav{position:absolute;left:440px;top:0;height:84px;display:flex}
.nav a{color:#fff;font-size:15px;text-decoration:none;padding:0 22px;line-height:84px}
.nav a.active{background:#fff;color:var(--ink);font-weight:700}

.hero{top:0;height:558px;background:radial-gradient(circle at 30% 60%,#aee53a 0,#7fc71a 45%,#56a70e 100%);overflow:hidden}
.bubble{position:absolute;border-radius:50%;background:rgba(255,255,255,.12)}
.hero h1{position:absolute;left:110px;top:236px;font-size:38px;font-weight:400;color:#fff;line-height:44px;letter-spacing:.5px}
.hero h1 strong{color:#1f5a06;font-weight:800}
.hero p{position:absolute;left:120px;top:328px;font-size:18px;color:#fff;line-height:24px}
.hero .cta{position:absolute;left:120px;top:397px;width:183px;height:41px;background:linear-gradient(#fff,#ddd);color:var(--ink);font-size:14px;font-weight:700;border-radius:3px;display:flex;align-items:center;justify-content:center}
.hero-icons{position:absolute;left:555px;top:200px;width:390px;height:250px;border-radius:120px;
  background:radial-gradient(ellipse at 50% 50%,rgba(30,70,90,.55) 0,rgba(40,90,110,.35) 45%,rgba(255,255,255,0) 72%)}
.hero-mascot{position:absolute;left:940px;top:95px;width:230px;height:470px;border-radius:110px 110px 40px 40px;
  background:linear-gradient(#8a5a32 0,#b07446 12%,#f0c9a4 20%,#f3d2b2 30%,#f7f9fa 42%,#e4ecef 70%,#8a9aa6 90%,rgba(120,130,140,0) 100%)}

/* our work */
.work{top:558px;height:351px;background:#fff}
.work .rule{position:absolute;left:0;top:199px;width:1200px;height:1px;background:#e6e6e6}
.service{position:absolute;top:162px;width:180px;text-align:center;font-size:12px;color:#555;line-height:16px}
.service .ico{width:80px;height:80px;border-radius:50%;margin:0 auto 18px;display:flex;align-items:center;justify-content:center;border:4px solid #fff;box-shadow:0 0 0 1px #ddd}
.ico.o{background:var(--orange)} .ico.g{background:var(--green)}

/* what we do */
.what{top:909px;height:426px;background:var(--soft);box-shadow:0 8px 10px -6px rgba(0,0,0,.25)}
.what h2{position:absolute;left:110px;top:30px;font-size:30px;color:var(--ink);font-weight:600}
.what .copy{position:absolute;left:110px;top:75px;width:530px;font-size:12.5px;line-height:18px;color:#777}
.what .copy b{color:var(--ink);font-weight:600}
.what .copy h3{font-size:15px;color:var(--ink);font-weight:600;margin:10px 0 3px}
.office-photo{position:absolute;left:690px;top:29px;width:402px;height:363px;border:1px solid #ccc;
  background:
    linear-gradient(90deg,transparent 0 12%,rgba(44,50,60,.9) 12% 22%,transparent 22% 28%,rgba(44,50,60,.9) 28% 38%,transparent 38% 44%,rgba(190,30,40,.8) 44% 52%,rgba(44,50,60,.9) 52% 62%,transparent 62% 68%,rgba(44,50,60,.9) 68% 80%,transparent 80%) 0 46%/100% 54% no-repeat,
    linear-gradient(#eef4f9 0,#bcd6ea 18%,#8fb7d8 40%,#a9b4bd 62%,#7d7f82 100%)}

/* team */
.team{top:1335px;height:445px}
.member{position:absolute;top:172px;width:130px;text-align:center;font-size:14px;font-weight:700;color:var(--ink)}
.member .avatar{width:106px;height:106px;border-radius:50%;margin:0 auto 20px;border:3px solid #fff;box-shadow:0 0 0 1px #ddd;
  background:radial-gradient(circle at 50% 36%,var(--skin) 0,#d9ae88 20%,rgba(230,230,230,0) 30%),linear-gradient(#ededed 0,#e6e6e6 62%,var(--suit) 70%,#1f242b 100%)}
.member .avatar.f{background:radial-gradient(circle at 50% 38%,var(--skin) 0,#d9ae88 18%,#4a2e1e 24%,rgba(230,230,230,0) 36%),linear-gradient(#ededed 0,#e6e6e6 64%,var(--suit) 72%,#1f242b 100%)}

/* testimonials */
.testi{top:1780px;height:493px;background:linear-gradient(#3ccaf4,#22b7ea)}
.testi h2{position:absolute;left:0;width:1200px;top:44px;text-align:center;color:#fff;font-size:30px;font-weight:400}
.testi .photo{position:absolute;left:546px;top:113px;width:110px;height:110px;border-radius:50%;border:4px solid #fff;
  background:radial-gradient(circle at 50% 50%,#f1d2b4 0,#e8c29e 28%,#e2c27a 42%,#c9a25a 70%,#f3f3f3 72%)}
.testi .name{position:absolute;left:0;width:1200px;top:250px;text-align:center;color:#222;font-size:20px}
.testi .quote{position:absolute;left:130px;width:940px;top:290px;text-align:center;color:#fff;font-size:12.5px;line-height:18px}
.dots{position:absolute;left:578px;top:375px;display:flex;gap:6px}
.dots i{width:9px;height:9px;border-radius:50%;background:#fff}
.dots i:first-child{background:#1b4d6a}

/* why */
.why{top:2273px;height:452px}
.why .lead{position:absolute;left:250px;width:700px;top:118px;text-align:center;font-size:12.5px;line-height:20px;color:#666}
.check{position:absolute;font-size:13px;color:#555;display:flex;align-items:center;gap:10px}
.check .box{width:15px;height:15px;border:1px solid #aaa;background:#fff;display:flex;align-items:center;justify-content:center}

/* ask */
.ask{top:2725px;height:481px;background:var(--soft)}
.field{position:absolute;left:108px;width:481px;height:42px;background:#fff;border:1px solid #d7d7d7;border-radius:3px;font-size:12px;color:#aaa;padding:13px 14px}
.message{position:absolute;left:632px;top:149px;width:460px;height:207px;background:#fff;border:1px solid #d7d7d7;border-radius:3px;font-size:12px;color:#aaa;padding:13px 14px}

/* footer */
footer{top:3206px;height:401px;background:var(--footer);color:var(--footer-text);font-size:12px}
.fcol{position:absolute;top:40px;width:220px}
.fcol h4{color:#fff;font-size:16px;font-weight:600;padding-bottom:12px;border-bottom:1px solid #333;margin-bottom:16px}
.flogo{display:flex;align-items:center;gap:8px;margin-bottom:12px}
.flogo .dot{width:22px;height:22px;border-radius:50%;background:var(--green)}
.flogo span{color:#fff;font-size:14px;font-weight:700}
.post{display:flex;gap:10px;margin-bottom:18px;line-height:17px}
.post small{display:block;color:#666;font-size:11px;margin-top:6px}
.contact-row{display:flex;gap:8px;margin-bottom:12px;line-height:17px}
.contact-row b{color:#bbb;font-weight:600}
.socials{display:flex;gap:6px;margin-top:8px}
.socials i{width:22px;height:22px;border-radius:50%;background:#666}
.fbottom{position:absolute;left:130px;width:940px;top:334px;border-top:1px solid #333;padding-top:22px;display:flex;justify-content:space-between;font-size:11.5px}
.fbottom nav a{color:#bbb;text-decoration:none;margin-left:6px}
.fbottom nav a.active{color:var(--lime)}
</style>
</head>
<body>

<section class="hero">
  <div class="bubble" style="left:-60px;top:120px;width:260px;height:260px"></div>
  <div class="bubble" style="left:380px;top:40px;width:180px;height:180px"></div>
  <div class="bubble" style="left:250px;top:430px;width:140px;height:140px"></div>
  <h1>HOW'S YOUR <strong>WEBSITE</strong><br><strong>WORKING FOR YOU?</strong></h1>
  <p>We Design Websites That Look Great...<br>&amp; Make Your Phone Ring!</p>
  <div class="cta">Free Website Analysis</div>
  <div class="hero-icons" role="img" aria-label="Illustrated cluster of marketing icons linked around a target"></div>
  <div class="hero-mascot" role="img" aria-label="Cartoon scientist mascot in a white lab coat"></div>
</section>

<header class="topbar">
  <div class="logo"><div class="logo-dot"></div><div class="logo-name">QuillBeaconWorks</div></div>
  <nav class="nav">
    <a class="active">HOME</a><a>Who we are</a><a>What we do</a><a>How it works</a><a>Why shoos us</a><a>Get in touch</a>
  </nav>
</header>

<section class="work">
  <div class="section-title" style="top:55px">Our Work</div>
  <div class="section-sub" style="top:95px">Lorem ipsum dolor sit amet, consectetur adipiscing elit.</div>
  <div class="rule"></div>
  <div class="service" style="left:102px">
    <div class="ico g"><svg width="38" height="34" viewBox="0 0 38 34" fill="none" stroke="#fff" stroke-width="3"><rect x="3" y="3" width="32" height="21" rx="2"/><path d="M19 24v6M11 31h16"/></svg></div>
    Web Design &amp;<br>Development</div>
  <div class="service" style="left:309px">
    <div class="ico o"><svg width="36" height="36" viewBox="0 0 36 36" fill="none" stroke="#fff" stroke-width="2.5"><circle cx="18" cy="18" r="15"/><ellipse cx="18" cy="18" rx="7" ry="15"/><path d="M3 18h30M6 10h24M6 26h24"/></svg></div>
    Local Search<br>Marketing</div>
  <div class="service" style="left:511px">
    <div class="ico o"><svg width="36" height="36" viewBox="0 0 36 36" fill="none" stroke="#fff" stroke-width="3.5"><circle cx="15" cy="15" r="10"/><path d="M22 22l10 10"/></svg></div>
    Search Engine<br>Optimization</div>
  <div class="service" style="left:716px">
    <div class="ico o"><svg width="38" height="36" viewBox="0 0 38 36" fill="none" stroke="#fff" stroke-width="2.5"><rect x="4" y="3" width="30" height="20"/><path d="M10 23l-4 11M28 23l4 11M19 23v9"/><text x="11" y="18" fill="#fff" stroke="none" font-size="11" font-family="Open Sans,sans-serif" font-weight="700">Ad</text></svg></div>
    ppc adveatising</div>
  <div class="service" style="left:920px">
    <div class="ico o"><svg width="36" height="34" viewBox="0 0 36 34" fill="none" stroke="#fff" stroke-width="2.5"><path d="M4 13h7l14-8v24l-14-8H4z"/><path d="M9 21l3 9M29 12v10"/></svg></div>
    mobile marketing</div>
</section>

<section class="what">
  <h2>What We Do.</h2>
  <div class="copy">
    <b>In a nutshell, we design websites that pop and develop marketing campaigns that rock!</b><br>
    First off, we get your website into tip top shape. If you don't have one, no problem...we can build you a hot new website loaded with goodies that help pump up your rankings and drive solid prospects to click on your website. Once there, carefully crafted marketing messages compel your visitors to connect with you by filling out your contact forms or dialing your digits.
    <h3>Turn “Clicks” into Customers!</h3>
    Yep, that's right...that's exactly what we do. And, oh, by the way...we do it at very affordable rates. Simply put, you'll get more prospects visiting your website and knocking on your business door per dollar spent with QuillBeaconWorks than with anyone else.
  </div>
  <div class="btn btn-orange" style="left:110px;top:342px;width:123px;height:38px">Read More</div>
  <div class="office-photo" role="img" aria-label="Photo of a business team in dark suits standing in a bright glass office"></div>
</section>

<section class="team">
  <div class="section-title" style="top:66px">Meet The Team</div>
  <div class="section-sub" style="top:106px">Lorem ipsum dolor sit amet, consectetur adipiscing elit.</div>
  <div class="member" style="left:125px"><div class="avatar" role="img" aria-label="Portrait photo of John Doe"></div>John Doe</div>
  <div class="member" style="left:289px"><div class="avatar f" role="img" aria-label="Portrait photo of Lusy"></div>Lusy</div>
  <div class="member" style="left:454px"><div class="avatar" role="img" aria-label="Portrait photo of James"></div>James</div>
  <div class="member" style="left:618px"><div class="avatar f" role="img" aria-label="Portrait photo of Emily"></div>Emily</div>
  <div class="member" style="left:779px"><div class="avatar" role="img" aria-label="Portrait photo of James"></div>James</div>
  <div class="member" style="left:943px"><div class="avatar f" role="img" aria-label="Portrait photo of Lusy"></div>Lusy</div>
  <div class="btn btn-green" style="left:529px;top:363px;width:142px;height:36px;font-size:14px">More About Us</div>
</section>

<section class="testi">
  <h2>TESTIMONIALS</h2>
  <div class="photo" role="img" aria-label="Portrait photo of client Jennifer"></div>
  <div class="name">Jennifer</div>
  <div class="quote">Lorem ipsum dolor sit amet, consectetur adipiscing elit, sed do eiusmod tempor incididunt ut labore et dolore magna aliqua. Ut enim ad minim veniam, dolore eu fugiat nulla pariatur. Excepteur sint occaecat cupidatat non proident, sunt in culpa le irure dolor in repreh te irure dolor in repreh te irure dolor in repreh qui officia deserunt mollit anim id est laborum.</div>
  <div class="dots"><i></i><i></i><i></i><i></i></div>
  <div class="btn btn-orange" style="left:488px;top:418px;width:222px;height:36px;font-size:14px">Read More Testimonials</div>
</section>

<section class="why">
  <div class="section-title" style="top:66px">Why Would You Choose Anyone Else?</div>
  <div class="lead">Here at QuillBeaconWorks, our team of creative website designers and clever internet marketing specialists work hard day in and day out to provide the highest quality of customer service and to maximize the return on your marketing dollars.</div>
  <div class="check" style="left:250px;top:210px"><span class="box"><svg width="13" height="11" viewBox="0 0 13 11"><path d="M1 6l4 4 7-9" stroke="#3f8a12" stroke-width="2.5" fill="none"/></svg></span>Consectetur adipiscing elit sed do eiusmod.</div>
  <div class="check" style="left:250px;top:248px"><span class="box"></span>Adipiscing elit sed do eiusmod tempor incididunt.</div>
  <div class="check" style="left:250px;top:289px"><span class="box"></span>Eiusmod tempor incididunt ut labore et dolore.</div>
  <div class="check" style="left:250px;top:327px"><span class="box"></span>Lorem ipsum dolor sit amet consectetur adipiscing.</div>
  <div class="check" style="left:250px;top:368px"><span class="box"></span>Dolor sit amet consectetur adipiscing elit sed.</div>
  <div class="check" style="left:604px;top:210px"><span class="box"><svg width="13" height="11" viewBox="0 0 13 11"><path d="M1 6l4 4 7-9" stroke="#3f8a12" stroke-width="2.5" fill="none"/></svg></span>Consectetur adipiscing elit sed do eiusmod.</div>
  <div class="check" style="left:604px;top:248px"><span class="box"></span>Adipiscing elit sed do eiusmod tempor incididunt.</div>
  <div class="check" style="left:604px;top:289px"><span class="box"></span>Eiusmod tempor incididunt ut labore et dolore.</div>
  <div class="check" style="left:604px;top:327px"><span class="box"></span>Lorem ipsum dolor sit amet consectetur adipiscing.</div>
  <div class="check" style="left:604px;top:368px"><span class="box"></span>Dolor sit amet consectetur adipiscing elit sed.</div>
</section>

<section class="ask">
  <div class="section-title" style="top:42px">Ask An Expert</div>
  <div class="section-sub" style="top:84px">You can get in touch with us any time you want</div>
  <div class="field" style="top:149px">Your Name</div>
  <div class="field" style="top:204px">Your Email Address</div>
  <div class="field" style="top:257px">Your Telephone Number</div>
  <div class="field" style="top:312px">Your Web Address</div>
  <div class="message">How May We Assist You?</div>
  <div class="btn btn-orange" style="left:517px;top:387px;width:164px;height:48px;font-size:18px;font-weight:700">Submit</div>
</section>

<footer>
  <div class="fcol" style="left:130px">
    <h4>About Us</h4>
    <div class="flogo"><i class="dot"></i><span>QuillBeaconWorks</span></div>
    <p style="line-height:17px">Lorem ipsum dolor sit amet, consectetur adipiscing elit sed do eiusmod tempor. Lorem ipsum dolor sit amet, consectetur adipiscing elit sed do eiusmod tempor incididunt ut labore et dolore magna aliqua. Ut enim ad minim veniam.</p>
  </div>
  <div class="fcol" style="left:368px">
    <h4>Latest Posts</h4>
    <div class="post"><svg width="14" height="14" viewBox="0 0 14 14"><path d="M2 12l2-5 6-6 3 3-6 6z" fill="#888"/></svg><div>Aliquip ex ea commodo consequat. Duis aute irure dolor in<small>March 10, 2012</small></div></div>
    <div class="post"><svg width="14" height="14" viewBox="0 0 14 14"><path d="M2 12l2-5 6-6 3 3-6 6z" fill="#888"/></svg><div>Aliquip ex ea commodo consequat. Duis aute irure dolor in<small>March 9, 2012</small></div></div>
  </div>
  <div class="fcol" style="left:608px">
    <h4>Latest Tweets</h4>
    <div class="post"><svg width="16" height="14" viewBox="0 0 16 14"><circle cx="8" cy="7" r="6" fill="#888"/></svg><div>Aliquip ex ea commodo consequat. Duis aute irure dolor in reprehendert in voluptate velit</div></div>
    <div class="post"><svg width="16" height="14" viewBox="0 0 16 14"><circle cx="8" cy="7" r="6" fill="#888"/></svg><div>Aliquip ex ea commodo consequat. Duis aute irure dolor in reprehendert in voluptate velit</div></div>
  </div>
  <div class="fcol" style="left:846px;width:240px">
    <h4>Contact Info</h4>
    <div class="contact-row"><svg width="12" height="16" viewBox="0 0 12 16"><path d="M6 1a5 5 0 0 0-5 5c0 4 5 9 5 9s5-5 5-9a5 5 0 0 0-5-5z" fill="#888"/><circle cx="6" cy="6" r="2" fill="#1f1f1f"/></svg><div><b>Address:</b> 415 W Larkspur Ave, Ste 310<br>Raleigh, NC 27603</div></div>
    <div class="contact-row"><svg width="12" height="14" viewBox="0 0 12 14"><path d="M2 1h3l1 3-2 1.5a8 8 0 0 0 3.5 3.5L9 7l3 1v3c0 1-1 2-2 2A10 10 0 0 1 1 3c0-1 0-2 1-2z" fill="#888"/></svg><div><b>Phone:</b> (800) 555-0148</div></div>
    <div class="contact-row"><svg width="12" height="14" viewBox="0 0 12 14"><rect x="1" y="4" width="10" height="8" fill="#888"/><rect x="3" y="1" width="6" height="4" fill="#888"/></svg><div><b>Fax:</b> (800) 555-0172</div></div>
    <div class="contact-row"><svg width="14" height="12" viewBox="0 0 14 12"><rect x="1" y="2" width="12" height="9" fill="#888"/><path d="M1 2l6 5 6-5" stroke="#1f1f1f" fill="none"/></svg><div><b>Email:</b> info@quillbeaconworks.com</div></div>
    <div style="color:#bbb;margin-top:6px">Follow Us</div>
    <div class="socials"><i></i><i></i><i></i><i></i><i></i><i></i><i></i></div>
  </div>
  <div class="fbottom">
    <span>Copyright © 2014. QuillBeaconWorks . All Rights Reserved.</span>
    <nav><a class="active">Home</a> | <a>Who we are</a> | <a>What we do</a> | <a>How it works</a> | <a>Why shoos us</a> | <a>Get in touch</a></nav>
  </div>
</footer>

</body>
</html>
```